Tidal Puffs. the aim is to sell vaping liquids based on mood or feelings

We are a company who sell vaping liquids. A designer from this site created a good logo for our company. I now need to use this logo and create a label to place onto vaping bottles. Unusually we will be selling vaping products based on Moods rather than flavours.

To be clear therefore the label should have our company Logo but then also reflect a particular type of Mood or feeling.

The designs for the various moods will then be printed as labels for our vaping bottles. We have 9 different Tidal Puffs (see below) that we intend to bring to the market and general public

i would therfore like designs for the following 9 feelings/moods:

Love
Chilled
Happy
Energy
Desire
Bliss
Lust
Calm
High

the first attachment has our stand alone Logo.

i will then send some attachments of ideas we were playing around with to point you in the right direction. i will need the designs to be very colourful and to reflect the mood.

i do like the love hart one so it doesn't necessarily mean that we need to have images of people on the label. i will leave it to the designers to use images they feel best reflects the specific mood

Target Market(s)

General public

Industry/Entity Type

Retail

Colors

Designer to choose colors to be used in the design.

Requirements
Must have
• my company logo on any design
Nice to have
• vibrant colours or image to match the particular mood vape

```html
<!DOCTYPE html>
<html lang="en">
<head>
<meta charset="utf-8">
<title>Tidal Puffs – Mood Labels</title>
<link href="https://fonts.googleapis.com/css2?family=Michroma&family=Pacifico&display=swap" rel="stylesheet">
<style>
  :root {
    --page: #ffffff;
    --label-bg: #050505;
    --gold: #cbbd82;
    --gold-dark: #8f8150;
    --brand: #e0457b;
    --bliss: #3f63c9;
    --calm: #9a4fd6;
    --chilled: #2fa48f;
    --desire: #c64fa6;
    --energy: #c88a3c;
    --high-a: #2fae55;
    --high-b: #d45a9a;
    --happy: #b9a340;
    --love: #d24a4e;
    --lust: #c04aa4;
  }
  * { box-sizing: border-box; margin: 0; padding: 0; }
  html, body { width: 1200px; height: 1200px; overflow: hidden; background: var(--page); }
  .sheet { position: relative; width: 1200px; height: 1200px; }

  .label {
    position: absolute;
    width: 248px;
    height: 247px;
    background: var(--label-bg);
    border: 3px solid var(--gold);
    box-shadow: inset 0 0 0 1px var(--gold-dark);
    overflow: hidden;
  }
  .label--r1 { top: 226px; }
  .label--r2 { top: 480px; }
  .label--r3 { top: 734px; }
  .label--c1 { left: 99px; }
  .label--c2 { left: 354px; }
  .label--c3 { left: 609px; }
  .label--c4 { left: 864px; }
  .label--center { left: 492px; }

  .smoke {
    position: absolute;
    inset: 0;
    background:
      radial-gradient(ellipse 60% 22% at 38% 78%, color-mix(in srgb, var(--tone) 55%, white) 0%, transparent 70%),
      radial-gradient(ellipse 70% 30% at 62% 40%, var(--tone2, var(--tone)) 0%, transparent 72%),
      radial-gradient(ellipse 90% 40% at 30% 60%, color-mix(in srgb, var(--tone) 70%, black) 0%, transparent 75%),
      var(--label-bg);
    opacity: 0.9;
  }

  .brand {
    position: absolute;
    top: 14px;
    left: 12px;
    display: flex;
    align-items: center;
    gap: 5px;
    font-family: "Michroma", sans-serif;
    font-size: 9px;
    color: var(--brand);
    letter-spacing: 0.02em;
  }
  .brand__dot {
    width: 9px; height: 9px;
    border-radius: 50%;
    background: var(--brand);
  }

  .mood {
    position: absolute;
    left: 0; right: 0;
    top: 50%;
    transform: translateY(-50%);
    text-align: center;
    font-family: "Michroma", sans-serif;
    font-size: 30px;
    letter-spacing: 0.16em;
    padding-left: 0.16em;
    color: var(--gold);
    text-shadow: 0 1px 0 var(--gold-dark);
  }
  .mood--long { font-size: 24px; letter-spacing: 0.1em; }
</style>
</head>
<body>
<main class="sheet">

  <section class="label label--r1 label--c1">
    <div class="smoke" style="--tone: var(--bliss)" role="img" aria-label="Swirling blue smoke on black"></div>
    <div class="brand"><span class="brand__dot"></span>Tidal Puffs</div>
    <h2 class="mood">BLISS</h2>
  </section>

  <section class="label label--r1 label--c2">
    <div class="smoke" style="--tone: var(--calm)" role="img" aria-label="Swirling violet smoke on black"></div>
    <div class="brand"><span class="brand__dot"></span>Tidal Puffs</div>
    <h2 class="mood">CALM</h2>
  </section>

  <section class="label label--r1 label--c3">
    <div class="smoke" style="--tone: var(--chilled)" role="img" aria-label="Swirling teal smoke on black"></div>
    <div class="brand"><span class="brand__dot"></span>Tidal Puffs</div>
    <h2 class="mood mood--long">CHILLED</h2>
  </section>

  <section class="label label--r1 label--c4">
    <div class="smoke" style="--tone: var(--desire)" role="img" aria-label="Swirling pink smoke on black"></div>
    <div class="brand"><span class="brand__dot"></span>Tidal Puffs</div>
    <h2 class="mood mood--long">DESIRE</h2>
  </section>

  <section class="label label--r2 label--c1">
    <div class="smoke" style="--tone: var(--energy)" role="img" aria-label="Swirling amber smoke on black"></div>
    <div class="brand"><span class="brand__dot"></span>Tidal Puffs</div>
    <h2 class="mood mood--long">ENERGY</h2>
  </section>

  <section class="label label--r2 label--c2">
    <div class="smoke" style="--tone: var(--high-b); --tone2: var(--high-a)" role="img" aria-label="Swirling green and pink smoke on black"></div>
    <div class="brand"><span class="brand__dot"></span>Tidal Puffs</div>
    <h2 class="mood">HIGH</h2>
  </section>

  <section class="label label--r2 label--c3">
    <div class="smoke" style="--tone: var(--happy)" role="img" aria-label="Swirling golden yellow smoke on black"></div>
    <div class="brand"><span class="brand__dot"></span>Tidal Puffs</div>
    <h2 class="mood">HAPPY</h2>
  </section>

  <section class="label label--r2 label--c4">
    <div class="smoke" style="--tone: var(--love)" role="img" aria-label="Swirling red smoke on black"></div>
    <div class="brand"><span class="brand__dot"></span>Tidal Puffs</div>
    <h2 class="mood">LOVE</h2>
  </section>

  <section class="label label--r3 label--center">
    <div class="smoke" style="--tone: var(--lust)" role="img" aria-label="Swirling magenta smoke on black"></div>
    <div class="brand"><span class="brand__dot"></span>Tidal Puffs</div>
    <h2 class="mood">LUST</h2>
  </section>

</main>
</body>
</html>
```